Corporate consulting business needs a business card

I want a professional business card.... surprise me

Updates

Reason: i dont think 2 days is enough

Target Market(s)

Corprorate and Not for Profit firms and organisations

Industry/Entity Type

Consulting

Contact Information for Business Card

Logo
Corporate Consulting Services
Clear Advice, Steady Delivery, Lasting Results
Tovan Presfield
Director
0427 31 94 62 (Larger)
tovan@tp-advisory.com.au
www.tp-advisory.com.au
include little icons beside the contact info:

- Envelope = email
- Phone = phone
- Globe = website

Font styles to use
Serif
Sans Serif

Requirements
Must have
• Professional and clean
Nice to have
• you tell me

```html
<!DOCTYPE html>
<html lang="en">
<head>
<meta charset="utf-8">
<title>TP Advisory Services – Business Card</title>
<link rel="stylesheet" href="https://fonts.googleapis.com/css2?family=Tinos:wght@400;700&family=Arimo:ital,wght@0,400;0,700;1,400&display=swap">
<style>
  :root {
    --bg: #ece9e5;
    --brown-dark: #5a2a0e;
    --brown: #7a3d16;
    --brown-light: #8e4c1f;
    --white: #ffffff;
    --paper: #f7f7f6;
    --ink: #1c1917;
    --muted: #f1e4d8;
  }
  * { margin: 0; padding: 0; box-sizing: border-box; }
  html, body { width: 1200px; height: 1023px; overflow: hidden; background: var(--bg); }
  .canvas { position: relative; width: 1200px; height: 1023px; }

  .card {
    position: absolute; left: 220px; width: 760px; height: 434px;
    border-radius: 22px; overflow: hidden; background: var(--paper);
    box-shadow: 0 10px 30px rgba(60, 35, 15, .18);
  }
  .card--front { top: 55px; }
  .card--back  { top: 534px; }

  .card__shape { position: absolute; inset: 0; width: 100%; height: 100%; }

  .brand { position: absolute; display: flex; align-items: center; gap: 16px; }
  .brand__dot { width: 30px; height: 30px; border-radius: 50%; border: 3px solid var(--brown); flex: none; }
  .brand__name {
    font-family: "Tinos", serif; font-weight: 400; color: var(--ink);
    letter-spacing: .5px; text-transform: uppercase; line-height: 1.15;
  }
  .card--front .brand { left: 40px; top: 178px; }
  .card--front .brand__name { font-size: 27px; }
  .card--back .brand { left: 0; right: 0; top: 150px; justify-content: center; }
  .card--back .brand__name { font-size: 44px; }
  .card--back .brand__dot { width: 40px; height: 40px; }

  .person { position: absolute; right: 44px; top: 42px; text-align: right; color: var(--white); font-family: "Arimo", sans-serif; }
  .person__name { font-size: 34px; font-weight: 700; }
  .person__role { font-size: 17px; margin-top: 4px; color: var(--muted); }

  .contact { position: absolute; left: 440px; top: 258px; list-style: none; font-family: "Arimo", sans-serif; color: var(--white); }
  .contact__item { display: flex; align-items: center; gap: 12px; font-size: 17px; margin-bottom: 14px; }
  .contact__item--phone { font-size: 21px; font-weight: 700; letter-spacing: 1px; }
  .contact__icon { width: 18px; height: 18px; flex: none; }

  .tagline {
    position: absolute; left: 0; right: 0; bottom: 0; height: 74px;
    background: linear-gradient(90deg, var(--brown-dark), var(--brown-light));
    color: var(--white); font-family: "Arimo", sans-serif; font-size: 21px;
    letter-spacing: .5px; display: flex; align-items: center; justify-content: center;
  }
</style>
</head>
<body>
<main class="canvas">

  <section class="card card--front" aria-label="Card front">
    <svg class="card__shape" viewBox="0 0 760 434" preserveAspectRatio="none" aria-hidden="true">
      <defs>
        <linearGradient id="brownFill" x1="0" y1="0" x2="1" y2="1">
          <stop offset="0" stop-color="#8e4c1f"/>
          <stop offset="1" stop-color="#5a2a0e"/>
        </linearGradient>
      </defs>
      <path d="M330 0 Q410 200 372 434 L760 434 L760 0 Z" fill="url(#brownFill)"/>
      <path d="M352 0 Q430 200 392 434" fill="none" stroke="#ffffff" stroke-width="5"/>
      <path d="M300 0 Q390 220 340 434" fill="none" stroke="#6b3414" stroke-width="6"/>
    </svg>

    <div class="brand">
      <span class="brand__dot"></span>
      <span class="brand__name">TP Advisory<br>Services</span>
    </div>

    <div class="person">
      <p class="person__name">Tovan Presfield</p>
      <p class="person__role">Director</p>
    </div>

    <ul class="contact">
      <li class="contact__item contact__item--phone">
        <svg class="contact__icon" viewBox="0 0 20 20" aria-hidden="true"><circle cx="10" cy="10" r="8.5" fill="none" stroke="#fff" stroke-width="1.5"/><path d="M7 5.5c-.8.6-1 1.8-.3 3.2 1 2 2.6 3.6 4.6 4.6 1.4.7 2.6.5 3.2-.3l-1.6-1.6-1.3.6c-1-.5-2-1.5-2.5-2.5l.6-1.3Z" fill="#fff"/></svg>
        0427 31 94 62
      </li>
      <li class="contact__item">
        <svg class="contact__icon" viewBox="0 0 20 20" aria-hidden="true"><rect x="2" y="4.5" width="16" height="11" fill="none" stroke="#fff" stroke-width="1.5"/><path d="M2 4.5l8 6.5 8-6.5" fill="none" stroke="#fff" stroke-width="1.5"/></svg>
        tovan@tp-advisory.com.au
      </li>
      <li class="contact__item">
        <svg class="contact__icon" viewBox="0 0 20 20" aria-hidden="true"><g fill="none" stroke="#fff" stroke-width="1.4"><circle cx="10" cy="10" r="8"/><ellipse cx="10" cy="10" rx="3.5" ry="8"/><path d="M2 10h16M3.5 6h13M3.5 14h13"/></g></svg>
        www.tp-advisory.com.au
      </li>
    </ul>
  </section>

  <section class="card card--back" aria-label="Card back">
    <div class="brand">
      <span class="brand__dot"></span>
      <span class="brand__name">TP Advisory Services</span>
    </div>
    <p class="tagline">Clear Advice, Steady Delivery, Lasting Results</p>
  </section>

</main>
</body>
</html>
```